Tallow Ridge Craft Cannabis Company

We need a one-page website designed for a craft cannabis website called "Tallow Ridge is a craft cannabis company" that will provide high-quality strains. It's located on tallowridge in Abbotsford British Columbia on lush green acreage. The facility takes pride in its modern technology bloom rooms to contain a healthy environment for high-quality handcrafted cannabis. We need a design that looks modern yet rustic- please do not add any marijuana leaves- We want the site to look professional as it is for investors. we will be selling products and do need the site to say "Coming soon"
Target Market(s)
investors and customers
Number of Pages Required
1 page
Font styles to use
Colors
Designer to choose colors to be used in the design.
Requirements
Must have
- greenery- its a cannabis production site with state of the art technology for growing. from seeds to full production it is a craft site with smaller rooms but high-end quality products. we need a tab that has a purchasing section another one for investors to watch our market trends and a page with our mission/ values and visions-
Nice to have
- showing people/ high end images/ greenspace/ farm (horticulture based)
Should not have
- no marijuana leaves

```html
<!DOCTYPE html>
<html lang="en">
<head>
<meta charset="utf-8">
<title>Tallow Ridge Craft Cannabis Company</title>
<link rel="stylesheet" href="https://fonts.googleapis.com/css2?family=Raleway:wght@400;500;600;700;800&family=Great+Vibes&display=swap">
<style>
:root{
  --green:#6cbf1a;
  --green-dark:#4f9a0e;
  --green-deep:#3f8a0a;
  --ink:#222;
  --text:#555;
  --muted:#888;
  --paper:#efedea;
  --white:#fff;
  --charcoal:#4a4a4a;
  --nav-active:#4b4b4b;
}
*{margin:0;padding:0;box-sizing:border-box}
html,body{width:1200px;height:3974px;overflow:hidden}
body{font-family:"Raleway",Arial,sans-serif;color:var(--text);background:var(--white);position:relative}
.section{position:absolute;left:0;width:1200px}
.abs{position:absolute}
.btn{position:absolute;background:var(--green);color:var(--white);font-weight:600;text-transform:uppercase;text-align:center;border:none}

/* header */
.site-header{top:0;height:106px;background:var(--white)}
.logo{left:125px;top:26px;color:var(--green);font-weight:800;font-size:36px;line-height:1}
.logo small{display:block;color:var(--charcoal);font-size:15px;font-weight:700;margin-top:4px}
.call{left:766px;top:42px;text-align:center}
.call .label{color:var(--green);font-size:15px;font-weight:700}
.call .number{color:var(--charcoal);font-size:17px;font-weight:600;margin-top:4px;display:flex;gap:8px;align-items:center}
.follow{left:968px;top:42px}
.follow .label{color:var(--green);font-size:15px;font-weight:700}
.follow .squares{display:flex;gap:4px;margin-top:8px}
.follow .squares span{width:14px;height:14px;background:var(--charcoal)}

/* nav */
.main-nav{top:106px;height:48px;background:var(--green)}
.main-nav ul{list-style:none;display:flex;position:absolute;left:148px;top:0;height:48px}
.main-nav li{height:48px;line-height:48px;padding:0 23px;color:var(--white);font-size:14px;font-weight:500;margin-right:22px}
.main-nav li.active{background:var(--nav-active);font-weight:700}

/* hero */
.hero{top:154px;height:548px;background:linear-gradient(180deg,#8a97a4 0%,#a3aab0 35%,#8c8e6a 55%,#5f7a2a 75%,#4e6b1c 100%)}
.hero .person{left:70px;top:30px;width:310px;height:518px;background:linear-gradient(180deg,#4a5058 0%,#2c3138 100%);border-radius:120px 120px 0 0;opacity:.85}
.hero-copy{left:583px;top:105px;color:var(--white)}
.hero-copy .welcome{font-family:"Great Vibes",cursive;font-size:54px;line-height:1}
.hero-copy h1{font-size:48px;font-weight:700;line-height:1.15;margin-top:4px}
.hero-copy .tag{font-size:30px;font-weight:600;margin-top:10px}
.hero-copy p{font-size:13px;line-height:1.5;width:440px;margin-top:14px}
.hero .btn{left:586px;top:404px;width:122px;height:34px;line-height:34px;font-size:12px}

/* about */
.about{top:702px;height:503px;background:var(--white)}
.sec-title{position:absolute;left:0;width:1200px;text-align:center;color:var(--green);font-size:28px;font-weight:500}
.rule{position:absolute;left:580px;width:40px;height:2px;background:#bbb}
.about .photo{left:167px;top:180px;width:384px;height:262px;background:linear-gradient(160deg,#dfe8e6 0%,#9fc38a 50%,#3d7a1e 100%);border:1px solid #ccc}
.about .copy{left:604px;top:180px;width:396px;font-size:13px;line-height:1.65}
.about .copy p+p{margin-top:14px}
.about .btn{left:604px;top:406px;width:118px;height:34px;line-height:34px;font-size:13px;text-transform:none}

/* features */
.features{top:1205px;height:398px;background:linear-gradient(135deg,#77c425 0%,#5fae14 50%,#6dbd1d 100%)}
.feature{top:106px;width:260px;color:var(--white)}
.feature .icon{margin-left:48px;height:60px}
.feature h3{font-size:18px;font-weight:800;margin-top:18px}
.feature p{font-size:13px;line-height:1.5;margin-top:10px;width:230px}

/* products */
.products{top:1603px;height:662px;background:var(--paper)}
.products .sec-title{top:70px;font-size:38px}
.products .sec-title b{color:var(--charcoal);font-weight:500}
.products .sub{position:absolute;left:0;width:1200px;top:125px;text-align:center;color:var(--green);font-style:italic;font-size:18px}
.product{top:241px;width:207px;text-align:center}
.product .img{width:207px;height:143px;border:1px solid #ddd}
.product h4{margin-top:38px;color:var(--ink);font-size:19px;font-weight:800}
.product p{margin-top:10px;font-size:12px;line-height:1.5;padding:0 4px}
.product .btn{position:static;display:inline-block;margin-top:16px;padding:0 10px;height:20px;line-height:20px;font-size:10px;font-weight:700}
.arrow{top:300px}

/* stats */
.stats{top:2265px;height:318px;background:var(--green)}
.stat{top:98px;width:200px;text-align:center;color:var(--white)}
.stat .num{font-size:52px;font-weight:700;line-height:1}
.stat .bar{width:40px;height:3px;background:var(--white);margin:10px auto}
.stat .lbl{font-size:16px;line-height:1.3}

/* testimonials */
.testimonials{top:2583px;height:583px;background:var(--paper)}
.testimonials .sec-title{top:92px;font-size:30px}
.quote{top:278px;width:403px;height:180px;background:var(--white);font-size:13px;line-height:1.7;text-align:center;padding:38px 30px}
.quote .mark{position:absolute;left:28px;bottom:22px}
.avatar{top:220px;width:60px;height:60px;border-radius:50%;background:#cfcfcf;border:3px solid var(--white)}
.who{top:238px;color:var(--green);font-weight:700;font-size:15px}

/* clients */
.clients{top:3166px;height:278px;background:var(--white)}
.clients .sec-title{top:64px;font-size:30px}
.client-row{position:absolute;left:222px;top:194px;width:760px;display:flex;justify-content:space-between;align-items:center}
.client-row span{color:var(--muted);font-weight:700;font-size:16px;display:flex;align-items:center;gap:6px}
.client-row i{width:12px;height:12px;border-radius:50%;background:#aaa;display:inline-block}

/* footer */
.grass{top:3444px;height:190px;background:linear-gradient(180deg,#ffffff 0%,#b9e08e 25%,#86cc3b 55%,var(--green) 100%)}
.site-footer{top:3634px;height:266px;background:var(--green);color:var(--white)}
.f-col{top:20px;font-size:13px;line-height:1.6}
.f-col h5{font-size:16px;font-weight:600;margin-bottom:16px;letter-spacing:.5px}
.f-brand{left:100px;width:200px;text-align:center}
.f-brand h5{font-weight:800;font-size:17px;line-height:1.25}
.f-brand p{font-size:11px;text-align:left;color:#eaf6d8}
.f-contact li{list-style:none;display:flex;gap:12px;margin-bottom:14px}
.f-about li{list-style:none;margin-bottom:10px}
.form{display:grid;grid-template-columns:150px 150px;gap:8px}
.form div{background:var(--white);color:var(--muted);height:36px;line-height:36px;padding-left:10px;font-size:13px}
.form .wide{grid-column:1 / span 2}
.form .send{background:#222;color:var(--white);width:126px;text-align:center;padding:0;font-weight:700;letter-spacing:1px}
.copyright{top:3900px;height:74px;background:var(--charcoal);color:#ccc;font-size:12px;text-align:center;line-height:74px}
</style>
</head>
<body>

<header class="section site-header">
  <div class="abs logo">Tallow Ridge<small>Craft Cannabis</small></div>
  <div class="abs call">
    <div class="label">Call Us now</div>
    <div class="number"><svg width="14" height="14" viewBox="0 0 24 24"><path fill="#6cbf1a" d="M6.6 10.8a15 15 0 0 0 6.6 6.6l2.2-2.2c.3-.3.7-.4 1-.2 1.1.4 2.3.6 3.6.6.6 0 1 .4 1 1V20c0 .6-.4 1-1 1A17 17 0 0 1 3 4c0-.6.4-1 1-1h3.5c.6 0 1 .4 1 1 0 1.3.2 2.5.6 3.6.1.3 0 .7-.2 1z"/></svg>(604) 555 0142</div>
  </div>
  <div class="abs follow">
    <div class="label">Follow Us</div>
    <div class="squares"><span></span><span></span><span></span><span></span></div>
  </div>
</header>

<nav class="section main-nav">
  <ul>
    <li class="active">Home</li><li>About Us</li><li>Products</li><li>Our Services</li><li>Investors</li><li>Testimonials</li><li>Contact us</li>
  </ul>
</nav>

<section class="section hero">
  <div class="abs" role="img" aria-label="Businesswoman standing in front of green crop fields under a grey sky" style="inset:0"></div>
  <div class="abs person" role="img" aria-label="Businesswoman in a dark suit with arms crossed"></div>
  <div class="abs hero-copy">
    <div class="welcome">Welcome to</div>
    <h1>Tallow Ridge Craft<br>Cannabis Company</h1>
    <div class="tag">High quality handcrafted cannabis</div>
    <p>Lorem ipsum dolor sit amet, consectetur adipiscing elit. Quid autem habent admirationis, cum prope accessers? An hoc usque quaque, aliter in vita? Non igitur de improbo, sed de callido improbo quaerimus, qualis Q.</p>
  </div>
  <div class="btn">Shop now</div>
</section>

<section class="section about">
  <h2 class="sec-title" style="top:84px">About Us</h2>
  <div class="rule" style="top:126px"></div>
  <div class="abs photo" role="img" aria-label="Two scientists inspecting plants inside a greenhouse"></div>
  <div class="abs copy">
    <p>We are located on tallowridge in Abbotsford British Columbia on lush green acreage. We take pride in our modern technology bloom rooms to contain a healthy environment for high-quality handcrafted cannabis.</p>
    <p>Lorem ipsum dolor sit amet, consectetur adipiscing elit. Quid autem habent admirationis, cum prope accessers? An hoc usque quaque, aliter in vita? Non igitur de improbo, sed de callido improbo quaerimus, qualis Q.</p>
  </div>
  <div class="btn">Read More</div>
</section>

<section class="section features">
  <div class="abs feature" style="left:212px">
    <svg class="icon" width="60" height="60" viewBox="0 0 60 60" fill="none" stroke="#fff" stroke-width="3"><path d="M8 56V24L30 8l22 16v32z"/><path d="M20 56V34h20v22M20 34l20 22M40 34L20 56"/></svg>
    <h3>MODERN FARM</h3>
    <p>Lorem ipsum dolor sit amet, consectetur adipiscing elit. Quid autem habent admiratio-nis, cum prope accessers?</p>
  </div>
  <div class="abs feature" style="left:506px">
    <svg class="icon" width="60" height="60" viewBox="0 0 60 60" fill="none" stroke="#fff" stroke-width="3"><path d="M30 56V8M18 56V18M42 56V18M10 56h40"/><path d="M30 16l-5-5M30 16l5-5M30 28l-5-5M30 28l5-5M18 28l-4-4M42 28l4-4"/></svg>
    <h3>100% ORGANIC</h3>
    <p>Lorem ipsum dolor sit amet, consectetur adipiscing elit. Quid autem habent admiratio-nis, cum prope accessers?</p>
  </div>
  <div class="abs feature" style="left:803px">
    <svg class="icon" width="64" height="60" viewBox="0 0 64 60" fill="none" stroke="#fff" stroke-width="3"><path d="M4 22h34v24H4zM38 30h12l8 8v8H38"/><circle cx="14" cy="48" r="5" fill="#6cbf1a"/><circle cx="48" cy="48" r="5" fill="#6cbf1a"/><circle cx="20" cy="12" r="9"/><path d="M20 7v5h4"/></svg>
    <h3>QUICK DELIVERY</h3>
    <p>Lorem ipsum dolor sit amet, consectetur adipiscing elit. Quid autem habent admiratio-nis, cum prope accessers?</p>
  </div>
</section>

<section class="section products">
  <h2 class="sec-title"><span>Our</span> <b>Products</b></h2>
  <div class="sub">Supplying only the very best</div>
  <svg class="abs arrow" style="left:120px" width="24" height="40" viewBox="0 0 24 40"><path d="M20 4L4 20l16 16" fill="none" stroke="#6cbf1a" stroke-width="2"/></svg>
  <svg class="abs arrow" style="left:1068px" width="24" height="40" viewBox="0 0 24 40"><path d="M4 4l16 16L4 36" fill="none" stroke="#6cbf1a" stroke-width="2"/></svg>
  <div class="abs product" style="left:196px">
    <div class="img" role="img" aria-label="Bottle of oil beside green plant cuttings" style="background:linear-gradient(180deg,#fff 0%,#f4e6c0 45%,#6ea83a 100%)"></div>
    <h4>LOREM IPSUM</h4>
    <p>Lorem ipsum dolor sit amet, con-sectetur adipiscing elit. Quid autem habent admirationis.</p>
    <div class="btn">Shop now</div>
  </div>
  <div class="abs product" style="left:500px">
    <div class="img" role="img" aria-label="Gloved hand holding dried buds over a glass jar" style="background:linear-gradient(180deg,#f2f2f2 0%,#d8d0c2 55%,#8fa1c9 100%)"></div>
    <h4>LOREM IPSUM</h4>
    <p>Lorem ipsum dolor sit amet, con-sectetur adipiscing elit. Quid autem habent admirationis.</p>
    <div class="btn">Shop now</div>
  </div>
  <div class="abs product" style="left:805px">
    <div class="img" role="img" aria-label="Row of amber dropper bottles" style="background:linear-gradient(90deg,#f7f3ee 0%,#c47a2e 40%,#a85f1a 70%,#f7f3ee 100%)"></div>
    <h4>LOREM IPSUM</h4>
    <p>Lorem ipsum dolor sit amet, con-sectetur adipiscing elit. Quid autem habent admirationis.</p>
    <div class="btn">Shop now</div>
  </div>
</section>

<section class="section stats">
  <div class="abs stat" style="left:236px"><div class="num">200</div><div class="bar"></div><div class="lbl">Acres of<br>Cultivation</div></div>
  <div class="abs stat" style="left:504px"><div class="num">15</div><div class="bar"></div><div class="lbl">years of<br>Experience</div></div>
  <div class="abs stat" style="left:761px"><div class="num">120</div><div class="lbl" style="font-size:12px;margin-top:2px">Company</div><div class="bar"></div><div class="lbl">Trusted supplier</div></div>
</section>

<section class="section testimonials">
  <h2 class="sec-title">What our clients say</h2>
  <div class="rule" style="top:142px"></div>
  <div class="abs quote" style="left:185px">Lorem ipsum dolor sit amet, consectetur adipiscing elit. Quid autem habent admirationis, cum prope accessers? An hoc usque quaque, aliter in vita?
    <svg class="mark" width="40" height="28" viewBox="0 0 40 28"><path d="M2 6h14v10l-6 12H4l5-12H2zM22 6h14v10l-6 12h-6l5-12h-7z" fill="#ddd"/></svg></div>
  <div class="abs quote" style="left:609px">Lorem ipsum dolor sit amet, consectetur adipiscing elit. Quid autem habent admirationis, cum prope accessers? An hoc usque quaque, aliter in vita?
    <svg class="mark" width="40" height="28" viewBox="0 0 40 28"><path d="M2 6h14v10l-6 12H4l5-12H2zM22 6h14v10l-6 12h-6l5-12h-7z" fill="#ddd"/></svg></div>
  <div class="abs avatar" style="left:190px" role="img" aria-label="Portrait of client Dana"></div>
  <div class="abs who" style="left:265px">Dana</div>
  <div class="abs avatar" style="left:614px" role="img" aria-label="Portrait of client Marek"></div>
  <div class="abs who" style="left:689px">Marek</div>
</section>

<section class="section clients">
  <h2 class="sec-title">our clients</h2>
  <div class="rule" style="top:110px"></div>
  <svg class="abs" style="left:142px;top:200px" width="14" height="24" viewBox="0 0 14 24"><path d="M12 2L2 12l10 10" fill="none" stroke="#aaa" stroke-width="2"/></svg>
  <svg class="abs" style="left:1044px;top:200px" width="14" height="24" viewBox="0 0 14 24"><path d="M2 2l10 10L2 22" fill="none" stroke="#aaa" stroke-width="2"/></svg>
  <div class="client-row">
    <span><i></i>Cedar Vale</span><span>Brightmoor</span><span>Halcyon</span><span><i></i>Wrenfield</span><span>Ferngate</span><span>Oakline</span>
  </div>
</section>

<div class="section grass" role="img" aria-label="Band of green grass blades rising into the footer"></div>

<footer class="section site-footer">
  <div class="abs f-col f-brand">
    <h5>Tallow Ridge<br>Craft Cannabis</h5>
    <p>Lorem ipsum dolor sit amet, con-sectetur adipiscing elit. Morbi auctor ullamcorper congue. Pha-sellus quis lacus quis ante ornare tincidunt lobortis sapien.</p>
  </div>
  <div class="abs f-col f-contact" style="left:336px">
    <h5>CONTACT US</h5>
    <ul>
      <li><svg width="14" height="18" viewBox="0 0 14 18"><path d="M7 0a7 7 0 0 1 7 7c0 5-7 11-7 11S0 12 0 7a7 7 0 0 1 7-7z" fill="#fff"/><circle cx="7" cy="7" r="2.5" fill="#6cbf1a"/></svg><span>418 Fernbrook Rd.<br>Suite 12<br>Abbotsford, BC V2S 0A1</span></li>
      <li><svg width="14" height="14" viewBox="0 0 24 24"><path fill="#fff" d="M6.6 10.8a15 15 0 0 0 6.6 6.6l2.2-2.2c.3-.3.7-.4 1-.2 1.1.4 2.3.6 3.6.6.6 0 1 .4 1 1V20c0 .6-.4 1-1 1A17 17 0 0 1 3 4c0-.6.4-1 1-1h3.5c.6 0 1 .4 1 1 0 1.3.2 2.5.6 3.6.1.3 0 .7-.2 1z"/></svg><span>800-555-0196</span></li>
      <li><svg width="14" height="12" viewBox="0 0 14 12"><rect width="14" height="12" fill="#fff"/><path d="M0 0l7 6 7-6" fill="none" stroke="#6cbf1a" stroke-width="1.5"/></svg><span>info@tallowridgecraftcannabis.com</span></li>
    </ul>
  </div>
  <div class="abs f-col f-about" style="left:607px">
    <h5>ABOUT US</h5>
    <ul><li>Home</li><li>Investors</li><li>Our mission</li><li>Values and visions</li></ul>
  </div>
  <div class="abs f-col" style="left:813px">
    <h5>GET IN TOUCH</h5>
    <div class="form">
      <div>Name</div><div>Phone</div>
      <div class="wide">Email address</div>
      <div class="send">SEND</div>
    </div>
  </div>
</footer>

<div class="section copyright">Copyright © 2017 tallowridgecraftcannabis - All Rights Reserved</div>

</body>
</html>
```